Business Card Design

Quorvel Software Limited develops and sells venue and event management software called Quorvel Stagehand, which is available in the cloud or on-premise. The company was established in 1986. Most of our customers are performing arts venues, museums and festivals. Our existing design is a bit dull. We need to convey that we are both innovative and reliable.
Not all our people show their mobile phone numbers on their cards, so the design needs to work land line and mobile or land line only.

Industry/Entity Type

Software

Contact Information for Business Card

Helen Brackwood
Director
Quorvel Software Limited
42B Millbank Lane, Epsom, Surrey, KT19 3DW
Telephone: +44 (0)1372 904213
Mobile: +44 (0)7700 900562
Email: hbrackwood@quorvel.example
Web: www.quorvel.example

```html
<!DOCTYPE html>
<html lang="en">
<head>
<meta charset="utf-8">
<title>Quorvel Software Limited – Business Card</title>
<link rel="stylesheet" href="https://fonts.googleapis.com/css2?family=Open+Sans:wght@400;600;700;800&display=swap">
<style>
  :root {
    --backdrop: #a7a8ac;
    --backdrop-light: #c4c5c8;
    --card-white: #ffffff;
    --brand-navy: #1d5580;
    --brand-blue: #2f7fb3;
    --band-deep: #0f4a78;
    --band-mid: #1f6596;
    --accent-line: #2d9ad8;
    --title-blue: #4a9bd1;
    --icon-blue: #7fbde6;
    --muted-grey: #a9adb2;
    --text-white: #ffffff;
  }
  * { box-sizing: border-box; margin: 0; padding: 0; }
  html, body { width: 1200px; height: 863px; overflow: hidden; }
  body {
    background: radial-gradient(ellipse at 50% 40%, var(--backdrop-light), var(--backdrop) 75%);
    font-family: "Open Sans", Arial, sans-serif;
    position: relative;
  }
  .card {
    position: absolute;
    left: 285px;
    width: 630px;
    height: 360px;
    background: var(--card-white);
    border-radius: 22px;
    overflow: hidden;
    box-shadow: 0 10px 28px rgba(0,0,0,0.22);
  }
  .card--front { top: 36px; }
  .card--back { top: 464px; }

  /* Brand lockup */
  .brand-line { display: flex; align-items: center; gap: 10px; }
  .brand-square { width: 26px; height: 26px; background: var(--brand-blue); flex: none; }
  .brand-name {
    font-weight: 800;
    color: var(--brand-navy);
    letter-spacing: 1px;
    white-space: nowrap;
  }

  /* Front */
  .front-brand { position: absolute; left: 52px; top: 128px; }
  .front-brand .brand-name { font-size: 30px; }
  .front-tagline { margin-top: 4px; font-size: 15px; color: #4d5157; }

  /* Back */
  .back-brand { position: absolute; left: 200px; top: 50px; }
  .back-brand .brand-square { width: 44px; height: 44px; }
  .back-brand .brand-name { font-size: 56px; line-height: 1; }
  .back-company-sub { margin: 6px 0 0 54px; font-size: 17px; color: var(--muted-grey); }

  .contact-band {
    position: absolute;
    left: 0; right: 0; bottom: 0;
    height: 168px;
    background: linear-gradient(90deg, var(--band-deep), var(--band-mid));
    border-top: 4px solid var(--accent-line);
    color: var(--text-white);
  }
  .person { position: absolute; left: 34px; top: 18px; }
  .person-name { font-size: 20px; font-weight: 800; letter-spacing: 0.5px; white-space: nowrap; line-height: 1.3; }
  .person-title { font-size: 14px; color: var(--title-blue); letter-spacing: 1px; }

  .address-block {
    position: absolute;
    left: 268px; top: 20px;
    font-size: 13.5px;
    line-height: 1.5;
    text-transform: uppercase;
    white-space: nowrap;
  }
  .contact-line { display: flex; align-items: center; gap: 8px; white-space: nowrap; }
  .contact-icon { width: 14px; height: 14px; flex: none; }
  .phones { position: absolute; left: 34px; top: 84px; font-size: 14.5px; line-height: 1.6; }
  .online { position: absolute; right: 30px; bottom: 18px; font-size: 14.5px; line-height: 1.6; }
</style>
</head>
<body>

  <section class="card card--front" aria-label="Card front">
    <div class="front-brand">
      <div class="brand-line">
        <span class="brand-square"></span>
        <span class="brand-name">QUORVEL</span>
      </div>
      <p class="front-tagline">venue and Event management software</p>
    </div>
  </section>

  <section class="card card--back" aria-label="Card back">
    <div class="back-brand">
      <div class="brand-line">
        <span class="brand-square"></span>
        <span class="brand-name">QUORVEL</span>
      </div>
      <p class="back-company-sub">Quorvel Software Limited</p>
    </div>

    <div class="contact-band">
      <div class="person">
        <p class="person-name">HELEN BRACKWOOD</p>
        <p class="person-title">DIRECTOR</p>
      </div>

      <div class="address-block">
        <p>Quorvel Software Limited</p>
        <p>42B Millbank Lane, Epsom, Surrey, KT19 3DW</p>
      </div>

      <div class="phones">
        <p class="contact-line">
          <svg class="contact-icon" viewBox="0 0 16 16" aria-hidden="true"><path fill="var(--icon-blue)" d="M2 5c0-2 2-3 6-3s6 1 6 3l-3 1-1-2H6L5 6 2 5zm2 2h8l2 6H2l2-6zm4 1.5a2 2 0 100 4 2 2 0 000-4z"/></svg>
          +44 (0)1372 904213
        </p>
        <p class="contact-line">
          <svg class="contact-icon" viewBox="0 0 16 16" aria-hidden="true"><rect x="4" y="1" width="8" height="14" rx="1.5" fill="none" stroke="var(--icon-blue)" stroke-width="1.6"/><circle cx="8" cy="12.5" r="0.9" fill="var(--icon-blue)"/></svg>
          +44 (0)7700 900562
        </p>
      </div>

      <div class="online">
        <p class="contact-line">
          <svg class="contact-icon" viewBox="0 0 16 16" aria-hidden="true"><rect x="1.5" y="3.5" width="13" height="9" fill="none" stroke="var(--icon-blue)" stroke-width="1.5"/><path d="M1.5 3.5L8 9l6.5-5.5" fill="none" stroke="var(--icon-blue)" stroke-width="1.5"/></svg>
          hbrackwood@quorvel.example
        </p>
        <p class="contact-line">
          <svg class="contact-icon" viewBox="0 0 16 16" aria-hidden="true"><circle cx="9.5" cy="6.5" r="4.2" fill="none" stroke="var(--icon-blue)" stroke-width="1.6"/><path d="M6.5 9.5L1.8 14.2" stroke="var(--icon-blue)" stroke-width="2"/></svg>
          www.quorvel.example
        </p>
      </div>
    </div>
  </section>

</body>
</html>
```